Vegan bakery needs business card

We need a business card design for my vegan bakery in Philadelphia Pa. We create amazing whole food plant based cuisine that is egg and dairy free. We use fruits, vegetables, healing herbs, nuts, natural sugars (date, turbinado, agave) and non bleached flours in our creations. Due to demand and interest in the Philadelphia area we created a late night vegan dessert delivery service named Tallowbrook Vegan. We are the only business providing delicious vegan desserts delivered to your door at 1am!! We would like to see designs that use the color scheme in the logo. The final design should communicate the benefits of our products: dairy/egg free, plant based, healing herbs, amazing food.

```html
<!DOCTYPE html>
<html lang="en">
<head>
<meta charset="utf-8">
<title>Gentlecrumb Desserts – Business Card</title>
<link rel="stylesheet" href="https://fonts.googleapis.com/css2?family=Dosis:wght@500;600&display=swap">
<style>
  :root {
    --backdrop: #ece7e2;
    --cocoa: #4b2b23;
    --cocoa-soft: #56332a;
    --paper: #ffffff;
    --coral: #e8684a;
    --leaf: #5aa637;
    --ink: #3a1f18;
    --cream: #fbf3ec;
  }
  * { margin: 0; padding: 0; box-sizing: border-box; }
  html, body {
    width: 1200px;
    height: 778px;
    overflow: hidden;
    background: var(--backdrop);
    font-family: "Dosis", sans-serif;
  }
  .canvas {
    position: relative;
    width: 1200px;
    height: 778px;
    display: flex;
    align-items: center;
    justify-content: center;
    gap: 60px;
  }
  .card {
    position: relative;
    width: 520px;
    height: 315px;
    border-radius: 22px;
    overflow: hidden;
    box-shadow: 0 10px 28px rgba(58, 31, 24, 0.18);
    display: flex;
    flex-direction: column;
    align-items: center;
  }

  /* Front */
  .card--front { background: var(--cocoa); color: var(--cream); justify-content: center; }
  .card__pattern {
    position: absolute;
    inset: 0;
    background: radial-gradient(circle at 30% 30%, var(--cocoa-soft), var(--cocoa) 70%);
  }
  .brand {
    position: relative;
    display: flex;
    align-items: center;
    gap: 12px;
    font-weight: 600;
    letter-spacing: 0.5px;
  }
  .brand__dot { width: 18px; height: 18px; border-radius: 50%; background: var(--coral); flex: none; }
  .card--front .brand { font-size: 38px; color: var(--cream); }
  .tagline {
    position: relative;
    margin-top: 22px;
    text-align: center;
    font-weight: 500;
    font-size: 25px;
    line-height: 1.1;
    color: var(--cream);
  }

  /* Back */
  .card--back { background: var(--paper); color: var(--ink); padding-top: 62px; }
  .card--back .brand { font-size: 34px; color: var(--coral); }
  .contact {
    margin-top: 50px;
    text-align: center;
    font-weight: 600;
    font-size: 15px;
    line-height: 1.45;
    color: var(--ink);
  }
  .social {
    display: flex;
    gap: 12px;
    margin-top: 26px;
    list-style: none;
  }
  .social__item { width: 20px; height: 20px; border-radius: 50%; background: var(--coral); }
</style>
</head>
<body>
  <main class="canvas">
    <section class="card card--front" aria-label="Business card front">
      <div class="card__pattern" role="img" aria-label="Faint line-drawn pattern of desserts and baked goods on chocolate brown"></div>
      <div class="brand"><span class="brand__dot"></span><span class="brand__name">Gentlecrumb Desserts</span></div>
      <p class="tagline">100% vegan<br>100% delicious</p>
    </section>

    <section class="card card--back" aria-label="Business card back">
      <div class="brand"><span class="brand__dot"></span><span class="brand__name">Gentlecrumb Desserts</span></div>
      <address class="contact" style="font-style: normal;">
        + 01 215 555 0147<br>
        info@gentlecrumbdesserts.com<br>
        www.gentlecrumbdesserts.com
      </address>
      <ul class="social" aria-label="Social profiles">
        <li class="social__item"></li>
        <li class="social__item"></li>
        <li class="social__item"></li>
      </ul>
    </section>
  </main>
</body>
</html>
```